Dailyvane Homepare Redesign - Arlo

After scores of designs were submitted in response to our recent PixelHarbor competition to re-think the Dailyvane.com homepage, we went back and looked at each of the artist’s portfolios. Several - including yours - were of particular interest to you.
We are now asking a handful of these designers to take a stab at a new Dailyvane.com homepage – again – but this time in accordance with some fresh guidelines. (See below.)
For this you will be paid $500 (US). We would need to have your work by Friday, March 4.
Furthermore, if we ask you to take your design through several additional stages, to a “final,” you will be paid an additional $750.
Please let us know as soon as possible if you are agreeable to this proposal.
What we have attached here are several wireframes that will help guide you to what we are after.
There are two wireframes, the first is that of the homepage. It has an area, at the top, that we are calling “the canvas”. The canvas will display different templates. The second wireframe features four different canvas templates.
We would like you to design one main homepage comp.
Once you are done with the homepage comp, please create 4 versions of it, each with a different canvas template in the “canvas” area.
Remember, the wireframes are for position only. Please use your creative judgment on colors, sizes, scale, styles, and graphics.
Generally speaking, it should be apparent that we seek a spare, clean look – easy to navigate, not too crowded with small images or unnecessary embellishment. Our audience tends to be older and not especially Web-savvy.
If you have any questions, do not hesitate to ask.
Will you participate in this project?

```html
<!DOCTYPE html>
<html lang="en">
<head>
<meta charset="utf-8">
<title>Dailyvane.com — Homepage</title>
<link href="https://fonts.googleapis.com/css2?family=Arimo:wght@400;700&display=swap" rel="stylesheet">
<style>
:root{
  --ink:#222;
  --text:#444;
  --muted:#666;
  --blue:#1a94d2;
  --blue-light:#4cc0ee;
  --blue-dark:#1585c4;
  --red:#e8140e;
  --red-dark:#c70f0a;
  --panel:#e6e9ec;
  --black:#000;
  --white:#fff;
}
*{box-sizing:border-box;margin:0;padding:0}
html,body{width:1200px;height:900px;overflow:hidden}
body{position:relative;background:var(--white);font-family:"Arimo",Arial,sans-serif;color:var(--ink)}
.abs{position:absolute}

/* top channels */
.channels{left:0;top:0;width:1200px;height:46px;background:var(--black)}
.channels a{position:absolute;top:11px;height:22px;line-height:22px;color:var(--white);font-size:13px;font-weight:700;text-decoration:none}
.channels a.active{background:var(--red);border-radius:3px;padding:0 14px}

/* header */
.masthead{left:0;top:46px;width:1200px;height:147px;background:linear-gradient(#f6f6f6,#d9d9d9)}
.brand{left:105px;top:75px;font-size:46px;font-weight:700;color:var(--blue);letter-spacing:-1px}
.tagline{left:323px;top:133px;font-size:12px;font-weight:700;color:var(--ink)}
.account{left:467px;top:90px;font-size:13px}
.account .bar{color:var(--ink);margin-right:16px}
.account a{color:var(--blue);font-weight:700}
.account .sep{color:var(--muted);margin:0 4px}
.welcome{left:490px;top:108px;font-size:11px;color:var(--ink)}
.hot{left:683px;top:77px;font-size:11px}
.hot h4{color:var(--red);font-size:11px;font-weight:700}
.hot ul{list-style:none;display:flex;margin-top:4px;color:#333}
.hot li+li::before{content:"|";color:#999;margin:0 6px}
.search{left:684px;top:111px;width:411px;height:24px;display:flex}
.search .field{flex:1;border:2px solid var(--red);border-right:0;background:var(--white);font-size:11px;color:var(--muted);padding:4px 9px}
.search .go{width:64px;background:linear-gradient(#ff4a3a,var(--red));color:var(--white);font-size:11px;font-weight:700;text-align:center;line-height:24px;border-radius:0 3px 3px 0}

/* main nav */
.nav{left:205px;top:156px;width:890px;height:37px;background:linear-gradient(var(--blue-light),var(--blue-dark));border-radius:0 4px 0 0}
.nav-tab{top:0;height:37px;line-height:37px;color:var(--white);font-size:13px;font-weight:700;text-align:center;border-right:1px solid rgba(255,255,255,.35)}
.nav-active{left:105px;top:152px;width:100px;height:41px;background:linear-gradient(#ff5a44,var(--red-dark));border-radius:4px 4px 0 0;color:var(--white);font-size:13px;font-weight:700;text-align:center;line-height:44px}

/* must reads */
.must{left:0;top:193px;width:1200px;height:37px;background:linear-gradient(var(--white),#e3e3e3);border-bottom:3px solid #eee;font-size:11px;font-weight:700}
.must .label{position:absolute;left:119px;top:12px;color:#1173b0;font-size:12px}
.must ul{position:absolute;left:198px;top:13px;list-style:none;display:flex}
.must li{padding:0 10px;border-left:1px solid #ccc}
.must li:first-child{padding-left:0;border-left:0}

/* feature */
.feature{left:105px;top:242px;width:990px;height:311px;background:var(--panel);padding:6px}
.feature-inner{width:100%;height:100%;background:var(--white);position:relative}
.photo{background:linear-gradient(135deg,#6b5a32,#2a2520 45%,#bf9a3c)}
.feature h1{position:absolute;left:416px;top:24px;font-size:20px;color:var(--blue);font-weight:700}
.feature ul{position:absolute;left:420px;top:53px;list-style:none;font-size:14px;color:#333}
.feature li{height:24px;padding-left:13px;position:relative}
.feature li::before{content:"";position:absolute;left:0;top:4px;border-left:6px solid var(--blue);border-top:4px solid transparent;border-bottom:4px solid transparent}

/* panels */
.panel{background:var(--panel);padding:6px}
.panel-inner{background:var(--white);height:100%;border:1px solid #d6dade;position:relative}
.panel-head{height:40px;background:linear-gradient(var(--blue-light),var(--blue-dark));color:var(--white);font-size:18px;font-weight:700;line-height:42px;padding-left:14px}
.thumb{background:linear-gradient(#9aa8c0,#2c3450)}
.story{position:absolute;left:16px;width:634px;height:91px;border-bottom:1px dotted #999}
.story .thumb{position:absolute;left:0;top:0;width:73px;height:58px}
.story h3{position:absolute;left:86px;top:4px;font-size:14px;color:var(--blue);font-weight:700}
.story p{position:absolute;left:87px;top:25px;font-size:12px;line-height:18px;color:var(--text);width:550px}

/* alerts */
.alerts{left:795px;top:566px;width:300px;height:179px;background:var(--red-dark);padding:6px}
.alerts-inner{height:100%;background:linear-gradient(#ff3a2a,#e8140e);position:relative;color:var(--white)}
.alerts h2{position:absolute;left:54px;top:17px;font-size:20px;font-weight:700}
.alerts label{position:absolute;width:48px;text-align:right;font-size:11px;font-weight:700;left:0}
.alerts .input{position:absolute;left:58px;width:213px;height:25px;background:var(--white);border:1px solid #999;color:var(--ink);font-size:11px;padding:5px 10px}
.alerts .btn{position:absolute;left:69px;top:127px;width:72px;height:24px;border-radius:4px;background:linear-gradient(var(--white),#cfcfcf);border:1px solid #888;color:var(--ink);font-size:12px;font-weight:700;text-align:center;line-height:22px}
</style>
</head>
<body>

<nav class="abs channels">
  <a class="active" style="left:105px">MONEY</a>
  <a style="left:210px">HEALTH</a>
  <a style="left:303px">WORLD</a>
  <a style="left:398px">TV</a>
  <a style="left:462px">VOICES</a>
</nav>

<header class="abs masthead"></header>
<div class="abs brand">Dailyvane.com</div>
<div class="abs tagline">Your Tagline Here</div>
<div class="abs account"><span class="bar">|</span><a>Sign In</a><span class="sep">|</span><a>Register</a></div>
<div class="abs welcome">Welcome to Dailyvane</div>
<div class="abs hot">
  <h4>Hot Topics:</h4>
  <ul><li>Lorem</li><li>Lipsum</li><li>Quisque</li><li>Vestibulum</li><li>Mauris</li></ul>
</div>
<div class="abs search"><div class="field">Enter Your Keword</div><div class="go">SEARCH</div></div>

<div class="abs nav">
  <div class="abs nav-tab" style="left:0;width:117px">United States</div>
  <div class="abs nav-tab" style="left:117px;width:83px">Politics</div>
  <div class="abs nav-tab" style="left:200px;width:93px">The Wire</div>
  <div class="abs nav-tab" style="left:293px;width:79px">Voices</div>
  <div class="abs nav-tab" style="left:372px;width:118px">Fast Features</div>
  <div class="abs nav-tab" style="left:490px;width:106px">Technology</div>
  <div class="abs nav-tab" style="left:596px;width:105px">Slideshows</div>
  <div class="abs nav-tab" style="left:701px;width:76px">Jokes</div>
  <div class="abs nav-tab" style="left:777px;width:56px;border-right:0">Cartoons</div>
</div>
<div class="abs nav-active">NewsFront</div>

<div class="abs must">
  <span class="label">Must Reads:</span>
  <ul>
    <li>Lorem ipsum dolor sit amet</li>
    <li>Nullam molestie ligula eni</li>
    <li>Vestibulum vel vestibulum tellus</li>
    <li>Integer lacinia erat vel sapien commodo</li>
  </ul>
</div>

<section class="abs feature">
  <div class="feature-inner">
    <div class="abs photo" role="img" aria-label="Photo of two men in suits at an awards lectern" style="left:16px;top:16px;width:380px;height:266px"></div>
    <h1>Vestibulu vestibanulum tellus uisque tempor commodo.</h1>
    <ul>
      <li>Pellentesque idleo that has haque id that haque idm ms er thatmpor anthat&nbsp; anec.</li>
      <li>Nullam molestie ligu ntesas&nbsp; haque idaque idhaque id quis enimel condimentum.</li>
      <li>Duis mattism molestie lig haque idaque iduh haque idst habeen quis eet convallis.</li>
      <li>Pellentesque atthat ntes haque idque idqen quierat posuere tempor anthat&nbsp; anec.</li>
      <li>Nullam mtt ehte sn haque haque id idtesque idleeteen quis enimel condimentum.</li>
      <li>Duis mattis iao that hasheh haque idt ist has been quisanie haque idet convallis.</li>
      <li>Nullam mntehat has att&nbsp; ligu haque idla ele haque ido atthn s enimel ondimentum.</li>
      <li>Pellenm molestie ligula ele that ha haque ids haque id thate tempor anthat&nbsp; anec.</li>
      <li>Nullam mntesqie ligula eleo thu haque ide idl haque ideo tt hasmel condimentum.</li>
    </ul>
  </div>
</section>

<section class="abs panel" style="left:105px;top:566px;width:676px;height:350px">
  <div class="panel-inner">
    <div class="panel-head">NewsFront</div>
    <article class="story" style="top:57px">
      <div class="thumb" role="img" aria-label="Portrait photo of a speaker"></div>
      <h3>Vestibulu vestibulum tellus that hasining the bashing uisque teipor ancommodo.</h3>
      <p>Vestibulum vehicula hendrerit interdum. Pellentesque id leo quis erat posuere tempor anthat&nbsp; anec nisanDuis mattis iaculis eros et convallis. Nullam molestie ligula enimel condimentum...</p>
    </article>
    <article class="story" style="top:148px">
      <div class="thumb" role="img" aria-label="Portrait photo of a speaker"></div>
      <h3>Vestibulu vestibulum tellus that hasining the bashing uisque teipor ancommodo.</h3>
      <p>Vestibulum vehicula hendrerit interdum. Pellentesque id leo quis erat posuere tempor anthat&nbsp; anec nisanDuis mattis iaculis eros et convallis. Nullam molestie ligula enimel condimentum...</p>
    </article>
    <article class="story" style="top:239px">
      <div class="thumb" role="img" aria-label="Portrait photo of a speaker"></div>
      <h3>Vestibulu vestibulum tellus that hasining the bashing uisque teipor ancommodo.</h3>
      <p>Vestibulum vehicula hendrerit interdum. Pellentesque id leo quis erat posuere tempor anthat&nbsp; anec nisanDuis mattis iaculis eros et convallis. Nullam molestie ligula enimel condimentum...</p>
    </article>
  </div>
</section>

<aside class="abs alerts">
  <div class="alerts-inner">
    <svg class="abs" style="left:12px;top:14px" width="34" height="24" viewBox="0 0 34 24" aria-hidden="true">
      <rect x="1" y="1" width="32" height="22" fill="#ffd21e" stroke="#c99a00"/>
      <path d="M1 1 L17 14 L33 1" fill="none" stroke="#c99a00" stroke-width="1.5"/>
    </svg>
    <h2>Sign up for News Alerts</h2>
    <label style="top:63px">Email:</label>
    <div class="input" style="top:51px">Enter Your Email ID</div>
    <label style="top:98px">Zip:</label>
    <div class="input" style="top:86px">Enter Your ZIP Code</div>
    <div class="btn">Sign Up</div>
  </div>
</aside>

<section class="abs panel" style="left:795px;top:758px;width:300px;height:160px">
  <div class="panel-inner">
    <div class="panel-head">Voices</div>
    <div class="abs thumb" role="img" aria-label="Portrait photo of a columnist" style="left:12px;top:55px;width:73px;height:58px"></div>
    <div class="abs" style="left:95px;top:57px;font-size:12px;font-weight:700;color:var(--blue)">Cras sollicitudin sodalesique.</div>
    <div class="abs" style="left:96px;top:76px;font-size:12px;color:var(--text)">By Corin Alde</div>
    <svg class="abs" style="left:96px;top:96px" width="15" height="13" viewBox="0 0 15 13" aria-hidden="true">
      <path d="M2 1h11a1 1 0 0 1 1 1v6a1 1 0 0 1-1 1H7l-3 3V9H2a1 1 0 0 1-1-1V2a1 1 0 0 1 1-1z" fill="#eee" stroke="#888"/>
    </svg>
    <div class="abs" style="left:116px;top:96px;font-size:11px;color:var(--muted)">72 <span style="text-decoration:underline">Comment</span>&nbsp; »</div>
    <div class="abs" style="left:12px;top:127px;width:258px;border-bottom:1px dotted #999"></div>
  </div>
</section>

</body>
</html>
```